Create modern and sleek business card for luxury real estate company

We're a "boutique" real estate office looking for a design that gets across a highly modern luxury brand. Blacks and whites are probably the best colors unless we try a silver foil for the logo. I've attached a version of our current logo here. I'd like to swap out the current font on there with Gotham Light Regular.

I'm looking to have one side of the card have the logo with the space for our agents info on the other side.

Target Market(s)

Young professionals in a "luxury" headspace

Industry/Entity Type

Real estate

Contact Information for Business Card

A place for agent name, cell number, website. The slogan "Simply Rethinking Real Estate".

Font styles to use
Other font styles liked:
• Gotham Regular

Colors

Designer to choose only greyscale colors for use in the design.

Requirements
Must have
• Matte black as the background color. Clean lines and use of contrast. A specific design aspect that will use silver foil.
Nice to have
• Up in the air on integrating a QR code
Should not have
• Any houses or other real estate related design (ex: a clip art house)

```html
<!DOCTYPE html>
<html lang="en">
<head>
<meta charset="utf-8">
<title>Lumen Estates – Business Card</title>
<link rel="stylesheet" href="https://fonts.googleapis.com/css2?family=Montserrat:wght@300;400;500;600;700&display=swap">
<style>
  :root {
    --stage: #dadada;
    --card: #000000;
    --silver: #d9d9d9;
    --silver-dim: #9a9a9a;
    --silver-bright: #f0f0f0;
    --font: "Montserrat", sans-serif;
  }
  * { margin: 0; padding: 0; box-sizing: border-box; }
  html, body {
    width: 1200px; height: 953px; overflow: hidden;
    background: var(--stage);
    font-family: var(--font);
  }
  .stage { position: relative; width: 1200px; height: 953px; }
  .card {
    position: absolute; top: 127px;
    width: 408px; height: 698px;
    background: var(--card);
    overflow: hidden;
  }
  .card--front { left: 181px; }
  .card--back { left: 611px; }

  .brand-ring {
    position: absolute; border-radius: 50%;
    border: 3px solid var(--silver);
  }
  .card--front .brand-ring { left: 149px; top: 110px; width: 122px; height: 122px; }
  .card--back .brand-ring { left: 168px; top: 133px; width: 74px; height: 74px; border-width: 2px; }

  .front-statement {
    position: absolute; left: 22px; bottom: 34px;
    font-size: 74px; font-weight: 300; line-height: 0.95;
    letter-spacing: 0.02em; text-transform: uppercase;
    color: var(--silver-bright);
  }

  .brand-name {
    position: absolute; left: 0; width: 100%; top: 220px;
    text-align: center;
    font-size: 26px; font-weight: 300; line-height: 31px;
    color: var(--silver);
    letter-spacing: 0.05em; text-transform: uppercase;
  }

  .agent { position: absolute; top: 362px; left: 0; width: 100%; text-align: center; }
  .agent-name {
    font-size: 23px; font-weight: 700; color: var(--silver);
    letter-spacing: 0.06em;
  }
  .agent-role {
    margin-top: 4px;
    font-size: 15px; font-weight: 400; color: var(--silver-dim);
    letter-spacing: 0.16em;
  }

  .contact { position: absolute; left: 87px; top: 470px; list-style: none; }
  .contact-item {
    display: flex; align-items: flex-start;
    font-size: 14px; font-weight: 500; color: var(--silver);
    letter-spacing: 0.08em; line-height: 23px;
    margin-bottom: 4px;
  }
  .contact-icon { width: 20px; height: 20px; margin-right: 11px; margin-top: 2px; flex: none; fill: var(--silver-dim); }
  .contact-icon--stroke { fill: none; stroke: var(--silver-dim); stroke-width: 1.5; }
</style>
</head>
<body>
<main class="stage">
  <section class="card card--front" aria-label="Card front">
    <div class="brand-ring"></div>
    <p class="front-statement">Lumen<br>Estates</p>
  </section>

  <section class="card card--back" aria-label="Card back">
    <div class="brand-ring"></div>
    <p class="brand-name">Lumen<br>Estates</p>

    <div class="agent">
      <p class="agent-name">Daniel Hart</p>
      <p class="agent-role">Managing Director</p>
    </div>

    <ul class="contact">
      <li class="contact-item">
        <svg class="contact-icon" viewBox="0 0 24 24" aria-hidden="true"><path d="M6.6 2.5l3 3.6-1.8 2.4c1.3 2.9 3.6 5.3 6.6 6.6l2.4-1.8 3.6 3c.4.3.4.9.1 1.3l-1.7 2.2c-.5.6-1.3.9-2 .7C9.8 19 5 14.2 3.5 7.2c-.2-.8.1-1.5.7-2l2.2-1.8c.1-.3.1-.9.2-.9z"/></svg>
        <span>+990 50 418 2763</span>
      </li>
      <li class="contact-item">
        <svg class="contact-icon contact-icon--stroke" viewBox="0 0 24 24" aria-hidden="true"><circle cx="12" cy="12" r="9"/><path d="M3 12h18M12 3c3 3 3 15 0 18M12 3c-3 3-3 15 0 18"/></svg>
        <span>www.lumenestates.com</span>
      </li>
      <li class="contact-item">
        <svg class="contact-icon contact-icon--stroke" viewBox="0 0 24 24" aria-hidden="true"><rect x="3" y="6" width="18" height="12"/><path d="M3 6l9 7 9-7M3 18l7-6M21 18l-7-6"/></svg>
        <span>hello@lumenestates.com</span>
      </li>
      <li class="contact-item">
        <svg class="contact-icon" viewBox="0 0 24 24" aria-hidden="true"><path d="M12 2a7 7 0 0 0-7 7c0 5 7 13 7 13s7-8 7-13a7 7 0 0 0-7-7zm0 9.5A2.5 2.5 0 1 1 12 6.5a2.5 2.5 0 0 1 0 5z"/></svg>
        <span>F2 Second Floor Palm Court<br>Coral Quay, Westmere</span>
      </li>
    </ul>
  </section>
</main>
</body>
</html>
```